Ridgeway Patrol Website Design

Hello Designers. I am an agency and am helping a security company get a better look. I have a new logo and a car done up. We are looking for a fresh look using the blue and the gold. Open to a complimentary color.

Here is the old site
https://moravanguard.com/

Here is another design for photos and everything. We weren't sold on it because we wanted to make it simple like the first one.

https://ww2.moravanguard.com/

Attached is also the copy I would like to put on there.

I am looking for tough, competent and simple. Our customers are contruction companies, event planners etc. It has to be clean and easy.

One thing we can't provide yet is photos. We are anticipating photos of our team with arms folded beside the car, close up of the owner with a logo'd shirt on. Pictures of an Ridgeway Patrol job site etc. (which most of the time is construction. They also do Mall security. You can see if you want to use stock photos for now.

I wanted to get the look of the front page done first. Hoping for something really awesome. Have fun.

```html
<!DOCTYPE html>
<html lang="en">
<head>
<meta charset="utf-8">
<title>Ridgeway Patrol — Security for New Brunswick Businesses and Events</title>
<link href="https://fonts.googleapis.com/css2?family=Oswald:wght@300;400;500&family=Poppins:wght@400;600&display=swap" rel="stylesheet">
<style>
:root{
  --navy:#0f1f33;
  --gold:#a07b2a;
  --ink:#1b2637;
  --body:#4b4f57;
  --grey:#eef0f2;
  --white:#ffffff;
}
*{box-sizing:border-box;margin:0;padding:0}
html,body{width:1200px;height:3326px;overflow:hidden;background:var(--white)}
body{position:relative;font-family:'Poppins',sans-serif;color:var(--body)}
.abs{position:absolute}
.display{font-family:'Oswald',sans-serif;font-weight:300;color:var(--navy);text-transform:uppercase;line-height:1}
.gold{color:var(--gold)}
.btn{position:absolute;background:var(--navy);color:#fff;font:600 12px 'Poppins',sans-serif;text-transform:uppercase;display:flex;align-items:center;justify-content:center;letter-spacing:.2px}

/* header */
.brand{left:88px;top:48px;display:flex;align-items:center;gap:14px}
.brand-mark{width:48px;height:48px;background:var(--navy)}
.brand-name{font:500 30px 'Oswald',sans-serif;color:var(--gold);text-transform:uppercase;letter-spacing:.5px}
.nav{right:236px;top:48px;display:flex;gap:23px;font-size:13.5px;color:var(--ink);text-transform:uppercase}
.nav-cta{left:989px;top:40px;width:122px;height:38px}
.side-dots{left:1154px;top:207px;width:4px}
.side-dots span{display:block;width:2px;height:50px;background:var(--navy);margin-bottom:10px}
.side-dots span:nth-child(2){background:#d6d8dc}

/* hero */
.hero-title{left:0;width:1200px;top:174px;text-align:center;font-size:56px;line-height:57px}
.hero-sub{left:0;width:1200px;top:304px;text-align:center;font-size:14px;color:var(--ink)}
.gold-band{left:0;top:602px;width:1200px;height:610px;background:var(--gold)}
.car-photo{left:88px;top:400px;width:1023px;height:323px;border-radius:140px 160px 40px 40px/120px 140px 40px 40px;background:linear-gradient(180deg,#e9eaec 0%,#d5d7da 55%,#b9bcc1 100%)}
.about-mark{left:162px;top:830px;width:320px;display:flex;align-items:center;gap:16px}
.about-mark i{width:40px;height:40px;background:#fff;flex:none}
.about-mark b{font:400 46px 'Oswald',sans-serif;color:#fff;text-transform:uppercase;line-height:1.1}
.about-copy{left:542px;top:806px;width:500px;color:#fff}
.about-copy h2{font:300 46px 'Oswald',sans-serif;text-transform:uppercase;margin-bottom:16px;line-height:1.1}
.about-copy p{font-size:13.5px;line-height:20.5px;margin-bottom:19px}

/* services */
.services-title{left:0;width:1200px;top:1310px;text-align:center;font-size:47px}
.service{top:1390px;width:246px;height:328px}
.service-label{position:absolute;left:33px;right:33px;bottom:28px;height:44px;background:rgba(12,18,28,.82);color:#fff;font:300 24px 'Oswald',sans-serif;text-transform:uppercase;display:flex;align-items:center;justify-content:center}

/* owned */
.grey-band{left:0;top:2293px;width:1200px;height:672px;background:linear-gradient(180deg,var(--grey) 0%,#f6f7f8 60%,#fff 100%)}
.owned-title{left:138px;top:1884px;font-size:46px;line-height:45px}
.owned-copy{left:138px;top:1992px;width:380px;font-size:13.5px;line-height:20.5px}
.owned-btn{left:138px;top:2140px;width:145px;height:39px}
.photo-frame{left:585px;top:1813px;width:491px;height:544px;background:#fff;box-shadow:0 30px 40px -20px rgba(0,0,0,.22)}
.guard-photo{left:598px;top:1826px;width:465px;height:518px;background:linear-gradient(160deg,#8d8e8c 0%,#4d4f51 45%,#1c1e22 100%)}

/* hiring */
.radio-photo{left:266px;top:2480px;width:250px;height:320px;background:linear-gradient(180deg,#3a3d42,#16181b);border-radius:18px}
.hiring-title{left:688px;top:2526px;font-size:46px}
.hiring-copy{left:688px;top:2592px;width:345px;font-size:13.5px;line-height:20.5px}
.hiring-btn{left:689px;top:2695px;width:146px;height:39px}

/* footer */
.footer{left:0;top:2965px;width:1200px;height:361px;background:var(--navy)}
.mailing{left:672px;top:2893px;width:528px;height:145px;background:var(--gold)}
.mailing h4{position:absolute;left:66px;top:30px;font:400 14px 'Oswald',sans-serif;color:#fff;text-transform:uppercase}
.mail-field{position:absolute;left:66px;top:54px;width:317px;height:56px;background:#fff;display:flex;align-items:center;padding-left:28px;gap:9px;font-size:13.5px;color:#555}
.mail-send{position:absolute;left:383px;top:54px;width:45px;height:56px;background:var(--navy);display:flex;align-items:center;justify-content:center}
.footer-brand{left:132px;top:3070px;width:210px;text-align:center}
.footer-brand i{display:block;width:60px;height:60px;background:#fff;margin:0 auto 14px}
.footer-brand b{font:500 32px 'Oswald',sans-serif;color:var(--gold);text-transform:uppercase;line-height:1.05}
.icon-box{width:39px;height:39px;background:#26364a;display:flex;align-items:center;justify-content:center;flex:none}
.contact{display:flex;gap:14px;color:#fff;font:300 15px 'Oswald',sans-serif;text-transform:uppercase;line-height:17px}
.contact span{padding-top:10px}
.socials{left:885px;top:3124px;display:flex;gap:6px}
.socials .icon-box i{width:12px;height:12px;background:#fff;display:block}
.footer-rule{left:0;top:3274px;width:1200px;height:1px;background:#27374c}
.copyright{left:0;top:3291px;width:1200px;text-align:center;color:#fff;font:300 13px 'Oswald',sans-serif;text-transform:uppercase}
.chat-btn{left:1081px;top:3252px;width:52px;height:52px;background:var(--gold);display:flex;align-items:center;justify-content:center}
</style>
</head>
<body>

<header>
  <div class="abs brand"><span class="brand-mark"></span><span class="brand-name">Ridgeway Patrol</span></div>
  <nav class="abs nav"><span>About</span><span>Careers</span><span>Services</span><span>Français</span></nav>
  <span class="btn nav-cta">Contact us</span>
  <div class="abs side-dots"><span></span><span></span><span></span></div>
</header>

<section>
  <h1 class="abs display hero-title"><span class="gold">Security</span> for New Brunswick<br>businesses and events</h1>
  <p class="abs hero-sub">Ridgeway Patrol is New Brunswick owned and operated. We are committed to make sure your tools,</p>
  <div class="abs gold-band"></div>
  <div class="abs car-photo" role="img" aria-label="Side view of a white patrol sedan wrapped with the company name and phone number"></div>
  <div class="abs about-mark"><i></i><b>Ridgeway<br>Patrol</b></div>
  <div class="abs about-copy">
    <h2>Ridgeway Patrol</h2>
    <p>We can meet any security need. Ridgeway Patrol is located in Marlow Bay, New Brunswick serving all of New Brunswick. We offer complete security services including event security, uniformed security and personal security services.</p>
    <p>No detail will be overlooked. Our employee training and screening process ensures that we have the right people. Our professional employees are given the tools to succeed. From crowd control to protecting people and property, our team is trained with industry best practices.</p>
    <p>We eliminate the guesswork for you by ensuring that we're up-to-date on all the regulations pertaining to public safety compliance.</p>
  </div>
</section>

<section>
  <h2 class="abs display services-title"><span class="gold">Ridgeway</span> Patrol Services</h2>
  <div class="abs service" style="left:88px;background:linear-gradient(160deg,#6d8da3,#2a3540 70%,#15191f)" role="img" aria-label="Event security officer in sunglasses with an earpiece"><span class="service-label">Event security</span></div>
  <div class="abs service" style="left:347px;background:linear-gradient(160deg,#56606b,#2c2f33 60%,#8a6a49)" role="img" aria-label="Retail security officer using a radio in front of monitors"><span class="service-label">Retail security</span></div>
  <div class="abs service" style="left:606px;background:linear-gradient(180deg,#6b6f73,#9aa0a6 40%,#d9742d 80%,#c35a1f)" role="img" aria-label="Construction site worker in hard hat and orange safety vest"><span class="service-label">Construction</span></div>
  <div class="abs service" style="left:865px;background:linear-gradient(160deg,#8a97a4,#3b4450 55%,#1a1e24)" role="img" aria-label="Investigator in a suit speaking into a radio"><span class="service-label">Investigations</span></div>
</section>

<section>
  <div class="abs grey-band"></div>
  <h2 class="abs display owned-title">New <span class="gold">Brunswick</span> owned<br>and operated</h2>
  <p class="abs owned-copy">Ridgeway Patrol is New Brunswick owned and operated. We are committed to make sure your tools, and hard earned assets don't get stolen. We are there to make sure your event runs smooth and unwanted situations are prevented and/or taken care of. You need eyes and ears 24/7. ...We are there. We're ready, so give us a call.</p>
  <span class="btn owned-btn">Find out more</span>
  <div class="abs photo-frame"></div>
  <div class="abs guard-photo" role="img" aria-label="Security officer in black cap and shirt speaking into a radio on a city street"></div>
</section>

<section>
  <div class="abs radio-photo" role="img" aria-label="Two black handheld two-way radios"></div>
  <h2 class="abs display hiring-title"><span class="gold">Now</span> hiring!</h2>
  <p class="abs hiring-copy">We're looking for 10 professional part-time and full-time security officers . We want hard-working, punctual individuals that want to be part of a supportive and enriching team.</p>
  <span class="btn hiring-btn">Find out more</span>
</section>

<footer>
  <div class="abs footer"></div>
  <div class="abs mailing">
    <h4>Join our mailing list</h4>
    <div class="mail-field">
      <svg width="13" height="10" viewBox="0 0 13 10"><rect x="0.5" y="0.5" width="12" height="9" fill="none" stroke="#aab"/><path d="M1 1l5.5 4.5L12 1" fill="none" stroke="#aab"/></svg>
      Enter your email address...
    </div>
    <div class="mail-send"><svg width="14" height="14" viewBox="0 0 14 14"><path d="M1 6.5L13 1 9 13 6.5 8z" fill="#fff"/></svg></div>
  </div>
  <div class="abs footer-brand"><i></i><b>Ridgeway Patrol</b></div>
  <div class="abs contact" style="left:415px;top:3124px">
    <div class="icon-box"><svg width="16" height="16" viewBox="0 0 16 16"><path d="M3 1l3 3-1.5 2a9 9 0 0 0 5.5 5.5L12 10l3 3-2 2C7 15 1 9 1 3z" fill="#fff"/></svg></div>
    <span>506.555.0142</span>
  </div>
  <div class="abs contact" style="left:621px;top:3124px">
    <div class="icon-box"><svg width="14" height="18" viewBox="0 0 14 18"><path d="M7 1a6 6 0 0 1 6 6c0 4-6 10-6 10S1 11 1 7a6 6 0 0 1 6-6z" fill="#fff"/><circle cx="7" cy="7" r="2.2" fill="#26364a"/></svg></div>
    <span>48 Harrow Quay Rd.<br>Suite 7<br>Marlow Bay NB<br>E9X 2K4</span>
  </div>
  <div class="abs socials">
    <div class="icon-box"><i></i></div><div class="icon-box"><i></i></div><div class="icon-box"><i></i></div><div class="icon-box"><i></i></div>
  </div>
  <div class="abs footer-rule"></div>
  <p class="abs copyright">© Copyright 2022 Ridgeway Patrol all rights reserved</p>
  <div class="abs chat-btn"><svg width="24" height="22" viewBox="0 0 24 22"><ellipse cx="13" cy="10" rx="9" ry="8" fill="#fff"/><path d="M4 21l3-6 4 3z" fill="#fff"/></svg></div>
</footer>

</body>
</html>
```